I need a business card for my original fine art pieces

I would like a business card design including a logo design for a new business in the art world. I am based in the Hunter Valley NSW Australia. I am a contemporary figurative, encaustic and wildlife artist. I would like to be able to upload my email and mobile number to this as well. This design should be one that I can incorporate into banners and flyers etc. Id like to incorporate one of my own images or partial image into the background or somewhere below. My initials are KD and I would like these used as a logo type. I would like the use of some colour and it to be bright and catchy. The final design should communicate artwork custom made and commissions available.

Overview: Original Fine Artworks for sale, online, art galleries etc, Custom made to order and by commission.

Target market is world wide audience and corporate world

My figurative work is painted using acrylics in a lot of natural ochre colours that reflect the Australian Outback, on canvas, linen, paper or board: My encaustic work is created in a contemporary abstract style using a blow torch and a made with a medium of 100% pure bees wax, Damar resin, mixed media and coloured pigments, applied to Birch board. My wildlife are created using coloured pencil and mixed media on a variety of paper types or board.

```html
<!DOCTYPE html>
<html lang="en">
<head>
<meta charset="utf-8">
<title>Kara Dawson – Business Card</title>
<link rel="stylesheet" href="https://fonts.googleapis.com/css2?family=Cinzel:wght@400;600&family=Montserrat:wght@500&display=swap">
<style>
  :root {
    --backdrop: #02adee;
    --card: #ffffff;
    --accent: #e8532a;
    --ink: #1f1a17;
    --sun-yellow: #f6dc3a;
    --warm-amber: #f4b42c;
    --cream: #fbe7b0;
    --deep-orange: #e4642a;
  }
  html, body {
    margin: 0;
    padding: 0;
    width: 1200px;
    height: 1200px;
    overflow: hidden;
    background: var(--backdrop);
  }
  .stage { display: block; width: 1200px; height: 1200px; }
  .card-face { fill: var(--card); }
  .placeholder-name {
    font-family: "Cinzel", serif;
    font-size: 40px;
    fill: var(--accent);
  }
  .contact-label {
    font-family: "Cinzel", serif;
    font-size: 25px;
    fill: var(--ink);
  }
  .icon-ring { fill: none; stroke: var(--ink); stroke-width: 3; }
  .icon-glyph { fill: var(--ink); }
  .icon-line { fill: none; stroke: var(--ink); stroke-width: 2.5; }
  .monogram-ring { fill: none; stroke: var(--accent); stroke-width: 5; }
  .monogram-text {
    font-family: "Cinzel", serif;
    font-weight: 400;
    font-size: 80px;
    fill: var(--accent);
  }
  .brand-name {
    font-family: "Cinzel", serif;
    font-weight: 600;
    font-size: 60px;
    fill: var(--accent);
  }
  .brand-tagline {
    font-family: "Montserrat", sans-serif;
    font-weight: 500;
    font-size: 23px;
    letter-spacing: 4.6px;
    fill: var(--ink);
  }
</style>
</head>
<body>
<svg class="stage" viewBox="0 0 1500 1500" xmlns="http://www.w3.org/2000/svg">
  <defs>
    <linearGradient id="front-warmth" x1="0" y1="0" x2="1" y2="0.6">
      <stop offset="0" stop-color="var(--sun-yellow)"/>
      <stop offset="0.35" stop-color="var(--cream)"/>
      <stop offset="0.6" stop-color="var(--warm-amber)"/>
      <stop offset="1" stop-color="var(--deep-orange)"/>
    </linearGradient>
    <linearGradient id="band-warmth" x1="0" y1="0" x2="1" y2="0">
      <stop offset="0" stop-color="var(--deep-orange)"/>
      <stop offset="0.15" stop-color="var(--warm-amber)"/>
      <stop offset="0.35" stop-color="var(--sun-yellow)"/>
      <stop offset="0.6" stop-color="var(--cream)"/>
      <stop offset="0.75" stop-color="var(--cream)"/>
      <stop offset="0.8" stop-color="var(--deep-orange)"/>
      <stop offset="1" stop-color="var(--deep-orange)"/>
    </linearGradient>
  </defs>

  <!-- Front: contact side -->
  <g class="card card--contact">
    <rect class="card-face" x="298" y="160" width="883" height="503"/>
    <polygon role="img" aria-label="Warm yellow and orange geometric artwork panel"
      fill="url(#front-warmth)"
      points="650,160 1181,160 1181,663 628,663 622,645 678,540 622,432 678,325 622,220"/>
    <text class="placeholder-name" x="335" y="430">YOUR NAME</text>

    <g class="contact-row">
      <circle class="icon-ring" cx="797" cy="285" r="25"/>
      <path class="icon-glyph" d="M797,271 L783,284 L787,284 L787,297 L794,297 L794,289 L800,289 L800,297 L807,297 L807,284 L811,284 Z"/>
      <text class="contact-label" x="836" y="287">ADDRESS</text>
    </g>
    <g class="contact-row">
      <circle class="icon-ring" cx="797" cy="369" r="25"/>
      <path class="icon-glyph" d="M786,358 c2,-2 5,-2 6,0 l3,5 c1,2 0,4 -2,5 c1,4 4,7 8,8 c1,-2 3,-3 5,-2 l5,3 c2,1 2,4 0,6 c-3,3 -8,4 -13,1 c-6,-4 -11,-9 -14,-15 c-2,-4 -1,-8 2,-11 z"/>
      <text class="contact-label" x="836" y="377">YOUR CALL</text>
    </g>
    <g class="contact-row">
      <circle class="icon-ring" cx="797" cy="456" r="25"/>
      <rect class="icon-glyph" x="782" y="446" width="30" height="20"/>
      <path d="M783,447 L797,458 L811,447 M783,465 L793,455 M811,465 L801,455" fill="none" stroke="#f6e6a0" stroke-width="2"/>
      <text class="contact-label" x="836" y="464">YOUR EMAIL</text>
    </g>
    <g class="contact-row">
      <circle class="icon-ring" cx="797" cy="537" r="25"/>
      <circle class="icon-line" cx="797" cy="537" r="13"/>
      <path class="icon-line" d="M784,537 H810 M797,524 C790,530 790,544 797,550 M797,524 C804,530 804,544 797,550"/>
      <text class="contact-label" x="836" y="543">YOUR WEBSITE</text>
    </g>
  </g>

  <!-- Back: brand side -->
  <g class="card card--brand">
    <rect class="card-face" x="298" y="853" width="869" height="497"/>
    <polygon role="img" aria-label="Warm geometric artwork band along the top edge"
      fill="url(#band-warmth)"
      points="298,853 1167,853 1167,935 1063,888 960,935 857,888 753,935 650,888 548,935 445,888 341,935 298,915"/>
    <polygon role="img" aria-label="Warm geometric artwork band along the bottom edge"
      fill="url(#band-warmth)"
      points="298,1295 348,1280 451,1322 553,1280 656,1322 758,1280 860,1322 963,1280 1065,1322 1167,1280 1167,1350 298,1350"/>

    <circle class="monogram-ring" cx="738" cy="1060" r="83"/>
    <text class="monogram-text" x="738" y="1089" text-anchor="middle">KD</text>

    <text class="brand-name" x="740" y="1198" text-anchor="middle">Kara Dawson</text>
    <text class="brand-tagline" x="740" y="1226" text-anchor="middle">ORIGINAL FINE ARTWORKS</text>
  </g>
</svg>
</body>
</html>
```